COVID-19 Related Signage for Hotel

Need to create new COVID-19 related signage utilizing our brand assets. Please use screenshots for copy/direction. essentially duplicate the screenshots but with our logo/branding.

All brand assets have been uploaded and examples of signage content. Pictures are not necessary but you can add them if you want similar to the examples attached.

Sign requirements

sign 1. Text "Hand Sanitizer Station" can add graphic
sign 2. Text "Protect Yourself" duplicate copy in the attached pictures
sign 3. Text "Face Mask Required" can add graphic
sign 4. Text "Face Covering Do's and Don'ts with text from "Face-covering checklist.jpg" REMOVE BWR logo or website or 3 face mask graphics
sign 5. Text "Maintain 6 Foot Distance" This sign will be printed and placed on the ground for guests to know where to stand in queue. Would prefer a circular Design. sign 6. Text "Wet, Lather, Scrub, Rinse, Dry" similar to screenshots attached.

ALL signs should have same look and feel throughout utilizing our brand graphics, logo, colors, and guidelines.

Target Market(s)

Hotel Guests

Industry/Entity Type

Hotel

Font styles to use
Sans Serif

Requirements
Must have
• Cohesive, unified branding look and feel

Should not have
• any use of the word "COVID-19" or Coronavirus.

```html
<!DOCTYPE html>
<html lang="en">
<head>
<meta charset="utf-8">
<title>Protect Yourself – Ridge Hollow Lodge</title>
<link href="https://fonts.googleapis.com/css2?family=Roboto+Condensed:wght@400&display=swap" rel="stylesheet">
<style>
  :root {
    --brand-orange: #f7731f;
    --band-grey: #ececec;
    --paper: #ffffff;
  }
  html, body {
    margin: 0;
    padding: 0;
    overflow: hidden;
    background: var(--paper);
  }
  .sign {
    position: relative;
    width: 848px;
    height: 1200px;
    overflow: hidden;
    background: var(--paper);
    font-family: "Roboto Condensed", "Arial Narrow", sans-serif;
    color: var(--brand-orange);
  }
  .pattern-band {
    position: absolute;
    left: 0;
    width: 100%;
  }
  .pattern-band--top {
    top: 0;
    height: 124px;
    background: var(--band-grey);
  }
  .pattern-band--bottom {
    bottom: 0;
    height: 57px;
    background: var(--brand-orange);
  }
  .brand-badge {
    position: absolute;
    left: 354px;
    top: 48px;
    width: 148px;
    height: 148px;
    border-radius: 50%;
    background: var(--brand-orange);
    display: flex;
    align-items: center;
    justify-content: center;
    text-align: center;
  }
  .brand-name {
    color: var(--paper);
    font-size: 21px;
    line-height: 1.1;
    letter-spacing: 0.5px;
  }
  .sign-title {
    position: absolute;
    left: 0;
    width: 100%;
    top: 278px;
    margin: 0;
    text-align: center;
    font-weight: 400;
    font-size: 58px;
    line-height: 1;
    letter-spacing: 1.5px;
    white-space: nowrap;
  }
  .title-rule {
    position: absolute;
    left: 118px;
    top: 346px;
    width: 615px;
    height: 5px;
    background: var(--brand-orange);
  }
  .tips {
    position: absolute;
    left: 116px;
    top: 430px;
    margin: 0;
    padding: 0;
    list-style: none;
  }
  .tip {
    position: relative;
    padding-left: 28px;
    height: 107px;
    font-size: 35px;
    line-height: 48px;
    letter-spacing: 1.4px;
    white-space: nowrap;
  }
  .tip::before {
    content: "";
    position: absolute;
    left: 2px;
    top: 19px;
    width: 7px;
    height: 7px;
    border-radius: 50%;
    background: var(--brand-orange);
  }
</style>
</head>
<body>
<main class="sign">
  <div class="pattern-band pattern-band--top" role="img" aria-label="Light grey decorative swirl pattern band"></div>

  <div class="brand-badge">
    <span class="brand-name">Ridge Hollow<br>Lodge</span>
  </div>

  <h1 class="sign-title">PROTECT YOURSELF</h1>
  <div class="title-rule"></div>

  <ul class="tips">
    <li class="tip">Stay Home if you’re feeling sick</li>
    <li class="tip">Cover your mouth</li>
    <li class="tip">Wash your hands for atleast 20 Seconds</li>
    <li class="tip">Keep distance 6-8 Ft.</li>
    <li class="tip">Clean surfaces regularly</li>
    <li class="tip">Dont touch face with unwashed hands</li>
  </ul>

  <div class="pattern-band pattern-band--bottom" role="img" aria-label="Orange decorative swirl pattern band"></div>
</main>
</body>
</html>
```